Poster for a Boat show

We need a poster for a boat show. Motorboats and Sailboats is presented in this Boat show (and other nautical topics like diving, wakeboard, kite, surf, fishing, ...)
This boat show is annual and the Poster is for the 2014 edition.

The style must be modern, dynamic.

Important Content:
Name of the boat show: Salon nautique des Brisants
Place: Halle VTR - Gare de Pirlou
Date: 7, 8 et 9 novembre 2014
Website: www.expo-flotvane.ch
Entrée gratuite • Restauration sur place
Please, leave a zone in the poster for sponsors logos

Secondary content (schedule):
07.11.2014 from 17h to 21h
08.11.2014 from 10h to 20h
09.11.2014 from 10h to 18h

It's necessary for us to have the source file (vector) for make, later, the different format (flyers, website, ...)

Exemple of design of other boat show:
http://www.exemple-revue-a.net/images/affiche-a.jpg
http://www.exemple-blog-b.com/images/affiche-b.jpg
http://www.exemple-hotel-c.com/images/affiche-c.jpg
http://www.exemple-port-d.com/images/affiche-d.jpg
http://www.exemple-folio-e.fr/images/affiche-e.png
http://www.exemple-info-f.fr/images/affiche-f.jpg
http://www.exemple-blog-g.com/images/affiche-g.jpg
http://www.exemple-surf-h.com/images/affiche-h.jpg
http://www.exemple-revue-i.net/images/affiche-i.jpeg

Target Market(s)

Nautical enthusiasts, more masculine, high income

Industry/Entity Type

Nautical

Font styles to use
Serif
Sans Serif

Requirements
Must have
• Motor and Sail boat approach

```html
<!DOCTYPE html>
<html lang="fr">
<head>
<meta charset="utf-8">
<title>Salon nautique des Brisants – Affiche 2014</title>
<link rel="stylesheet" href="https://fonts.googleapis.com/css2?family=Antonio:wght@700&family=Roboto+Condensed:wght@400;700&display=swap">
<style>
  :root {
    --navy: #0d4a8c;
    --navy-deep: #0a3d78;
    --sky: #1aa3e8;
    --sky-light: #8fd0f5;
    --sea: #0b3f9e;
    --paper: #ffffff;
    --backdrop-center: #ffffff;
    --backdrop-edge: #d6d6d6;
    --ink: #111111;
  }
  * { box-sizing: border-box; margin: 0; padding: 0; }
  html, body { width: 1200px; height: 1000px; overflow: hidden; }
  body {
    position: relative;
    background: radial-gradient(ellipse at 50% 45%, var(--backdrop-center) 0%, #f2f2f2 45%, var(--backdrop-edge) 100%);
    font-family: "Roboto Condensed", "Arial Narrow", sans-serif;
  }

  .poster {
    position: absolute;
    left: 322px; top: 37px;
    width: 597px; height: 844px;
    background: var(--paper);
    box-shadow: 0 3px 8px rgba(0,0,0,0.35);
  }

  .photo { position: absolute; }

  .hero {
    left: 8px; top: 1px; width: 580px; height: 271px;
    overflow: hidden;
    background: linear-gradient(120deg, #0d5fb8 0%, #2f8fe0 35%, #a9dcf7 60%, #4aa8ea 80%, #1670cc 100%);
  }
  .title {
    position: absolute;
    left: 30px; top: 2px;
    font-family: "Antonio", "Oswald", sans-serif;
    font-weight: 700;
    font-size: 116px;
    line-height: 124px;
    color: var(--paper);
    white-space: nowrap;
    transform: scaleX(0.8);
    transform-origin: left top;
    text-shadow:
      0 0 2px var(--sky), 3px 0 0 var(--sky), -3px 0 0 var(--sky),
      0 3px 0 var(--sky), 0 -3px 0 var(--sky),
      2px 2px 0 var(--sky), -2px -2px 0 var(--sky),
      2px -2px 0 var(--sky), -2px 2px 0 var(--sky);
  }

  .info {
    position: absolute;
    left: 8px; top: 302px; width: 285px;
    text-align: center;
    color: var(--navy);
  }
  .venue {
    font-weight: 700;
    font-size: 44px;
    line-height: 52px;
    letter-spacing: -0.5px;
  }
  .dates {
    margin-top: 8px;
    font-weight: 700;
    font-size: 86px;
    line-height: 80px;
    letter-spacing: -1px;
  }
  .dates sup {
    font-size: 26px;
    vertical-align: 42px;
    margin: 0 10px 0 2px;
  }
  .month {
    font-weight: 700;
    font-size: 34px;
    line-height: 44px;
    letter-spacing: -0.5px;
  }
  .catering {
    margin: 14px auto 0;
    width: 259px; height: 28px;
    background: var(--navy);
    color: var(--paper);
    font-size: 18px;
    line-height: 28px;
    letter-spacing: 0.3px;
  }
  .website {
    margin-top: 6px;
    font-size: 18px;
    line-height: 22px;
  }

  .winch {
    left: 304px; top: 282px; width: 284px; height: 273px;
    background: linear-gradient(160deg, #b9dcf3 0%, #3f7fc4 35%, #17263f 60%, #dfe8f0 85%, #ffffff 100%);
  }
  .knot {
    left: 8px; top: 642px; width: 285px; height: 198px;
    background: linear-gradient(135deg, #f2f2f2 0%, #c8d4e2 30%, #1f5fb8 55%, #0c3f9a 100%);
  }

  .schedule {
    position: absolute;
    left: 304px; top: 566px; width: 292px; height: 226px;
    background: linear-gradient(180deg, #bfe0f7 0%, #e8f4fc 35%, #f3f8fb 55%, #7fa7c9 66%, #1c55a8 75%, var(--sea) 100%);
    color: var(--navy-deep);
    text-align: center;
  }
  .schedule h2 {
    margin-top: 16px;
    font-weight: 700;
    font-size: 25px;
    line-height: 28px;
  }
  .schedule ul {
    list-style: none;
    margin-top: 6px;
    font-size: 20px;
    line-height: 25px;
  }

  .sponsor-note {
    position: absolute;
    left: 938px; top: 808px;
    display: flex; align-items: center;
    color: var(--ink);
    font-size: 22px;
  }
  .sponsor-note svg { margin-right: 14px; }
</style>
</head>
<body>
  <main class="poster">
    <div class="photo hero" role="img" aria-label="Photo de voiles blanches et mât d'un voilier sur ciel bleu">
      <h1 class="title">Salon nautique<br>des Brisants</h1>
    </div>

    <section class="info">
      <p class="venue">Halle VTR -<br>Gare de Pirlou</p>
      <p class="dates">7,8<sup>ET</sup>9</p>
      <p class="month">NOVEMBRE 2014</p>
      <p class="catering">RESTAURATION SUR PLACE</p>
      <p class="website">www.expo-flotvane.ch</p>
    </section>

    <div class="photo winch" role="img" aria-label="Photo d'un winch de voilier enroulé de cordage bleu marine"></div>

    <section class="schedule" role="img" aria-label="Horaires sur photo de lac et montagnes avec voiliers">
      <h2>Schedule:</h2>
      <ul>
        <li>07.11.2014 from 17h to 21h</li>
        <li>08.11.2014 from 10h to 20h</li>
        <li>09.11.2014 from 10h to 18h</li>
      </ul>
    </section>

    <div class="photo knot" role="img" aria-label="Photo d'un nœud de cordage blanc sur fond bleu"></div>
  </main>

  <div class="sponsor-note">
    <svg width="33" height="32" viewBox="0 0 33 32" aria-hidden="true"><polygon points="0,16 33,0 33,32" fill="#111111"/></svg>
    <span>sponser section</span>
  </div>
</body>
</html>
```